Real Estate Marketing Company Needs 1 Page 8.5x11 Price List Flyer Design

We need a 1 page 8.5in x 11in price list flyer that is intended for drop off at local offices. This is intended to show all the services we offer including pricing to potential new clients. It should be separated into sections for the different services we offer. I'd also like some photos and our Logo on the list to make it look nice so its not all text. Try to incorporate the logo colors in the design.

Industry/Entity Type

Real Estate

Requirements
Must have
• Price List
• Photos
• Logo
• website address

```html
<!DOCTYPE html>
<html lang="en">
<head>
<meta charset="utf-8">
<title>Price List Flyer</title>
<link rel="stylesheet" href="https://fonts.googleapis.com/css2?family=Cinzel:wght@400;600&family=Open+Sans:wght@400;600;700&display=swap">
<style>
  :root {
    --backdrop: #e6e6e6;
    --brand-red: #b11f2a;
    --band-gray: #bdbdbd;
    --bar-gray: #c9c9c9;
    --ink-white: #ffffff;
    --ink-dark: #3a3a3a;
    --sky: #4f8fd6;
    --stone: #c9b79a;
    --garden: #5e7d3a;
    --pool: #4fb3cf;
  }
  * { box-sizing: border-box; margin: 0; padding: 0; }
  html, body { width: 1200px; height: 712px; overflow: hidden; }
  body {
    background: var(--backdrop);
    font-family: "Open Sans", Arial, sans-serif;
    display: flex; align-items: center; justify-content: center;
  }
  .flyer {
    width: 525px; height: 680px;
    background: var(--brand-red);
    display: flex; flex-direction: column;
    box-shadow: 0 2px 8px rgba(0,0,0,.15);
  }
  .title-band {
    height: 44px; background: var(--band-gray);
    border-bottom: 4px solid var(--brand-red);
    display: flex; align-items: center; padding-left: 18px;
  }
  .title-band h1 {
    font-family: "Cinzel", Georgia, serif; font-weight: 400;
    color: var(--ink-white); font-size: 24px; letter-spacing: 1px;
  }
  .photo-collage { position: relative; height: 250px; }
  .photo-main {
    position: absolute; inset: 0;
    background: linear-gradient(180deg, var(--sky) 0%, #9cc3ea 28%, var(--stone) 48%, #a89070 62%, var(--garden) 78%, var(--pool) 100%);
  }
  .photo-inset { position: absolute; right: 0; width: 120px; border: 2px solid var(--ink-white); }
  .photo-inset.garden { top: 92px; height: 74px; background: linear-gradient(160deg, #3f6b2a, #7fa05a 60%, #a8b6c4); }
  .photo-inset.interior { top: 166px; left: 210px; right: auto; width: 195px; height: 84px; background: linear-gradient(170deg, #e8e2d6, #c7b49a 55%, #6f8a4a); }
  .photo-inset.patio { top: 166px; height: 84px; background: linear-gradient(170deg, #d9cfbf, #b08a62 60%, #4d6d36); }
  .brand-box {
    position: absolute; left: 300px; top: 182px; width: 104px; height: 60px;
    background: var(--ink-white);
    display: flex; flex-direction: column; align-items: center; justify-content: center; gap: 4px;
  }
  .brand-dot { width: 18px; height: 18px; border-radius: 50%; background: var(--brand-red); }
  .brand-name { font-size: 10px; font-weight: 700; color: var(--ink-dark); text-align: center; line-height: 1.1; }
  .price-list {
    flex: 1; display: grid; grid-template-columns: 1fr 1fr; gap: 0 22px;
    padding: 14px 18px 0; color: var(--ink-white); font-size: 10.5px; line-height: 1.45;
  }
  .section-bar {
    background: var(--bar-gray); color: var(--ink-white);
    font-weight: 700; font-size: 11px; text-align: center;
    padding: 2px 0; margin: 8px 0 6px;
  }
  .price-list .column > .section-bar:first-child { margin-top: 0; }
  .price-list strong { font-weight: 700; }
  .price-list p { margin-bottom: 3px; }
  .note { margin-top: 4px; }
  .contact {
    color: var(--ink-white); font-weight: 700; font-size: 12.5px;
    text-align: center; padding: 0 18px 16px; line-height: 1.45;
  }
  .footer-band { height: 14px; background: var(--band-gray); }
</style>
</head>
<body>
  <main class="flyer">
    <header class="title-band"><h1>Presentation Is Everything</h1></header>

    <section class="photo-collage">
      <div class="photo-main" role="img" aria-label="Photo of a large stone estate home with a pool and landscaped garden"></div>
      <div class="photo-inset garden" role="img" aria-label="Photo of a garden view"></div>
      <div class="photo-inset interior" role="img" aria-label="Photo of a bright interior with patio doors"></div>
      <div class="photo-inset patio" role="img" aria-label="Photo of an outdoor patio"></div>
      <div class="brand-box">
        <span class="brand-dot"></span>
        <span class="brand-name">Open Gate Photography</span>
      </div>
    </section>

    <section class="price-list">
      <div class="column">
        <div class="section-bar">Package Pricing</div>
        <p><strong>Silver Package:</strong> 15 Photos + Floor Plan (3,500 sqft) - $225</p>
        <p><strong>Gold Package:</strong> 25 Photos + Floor Plan (4,500 sqft) - $300</p>
        <p><strong>Platinum Package:</strong> 35 Photos + Floor Plan (5,500 sqft) - $375</p>
        <div class="section-bar">Photography Only</div>
        <p>15 Photo Bundle: $100<br>25 Photo Bundle: $150<br>35 Photo Bundle: $200</p>
        <div class="section-bar">Additional Services</div>
        <p><strong>Aerial Photos:</strong> 3-6 Photos - $200<br>($75 if combined with another package)</p>
      </div>
      <div class="column">
        <p><strong>Aerial Video:</strong> (1-3 min video) - $375</p>
        <p><strong>Branded Video Tour w/ Aerial Video:</strong> (2-4 min video of property) - $800-$1300 (voiceover optional - call for details)</p>
        <p><strong>Twilight Photos:</strong> 3-6 Photos - $225</p>
        <p><strong>Luxury Package:</strong> $2,000 (includes all services listed)</p>
        <div class="section-bar">Floor Plans</div>
        <p>Floor Plan (3,500 sqft) - $150<br>Floor Plan (4,500 sqft) - $175<br>Floor Plan (5,500 sqft) - $200<br>*$25 per additional 500sqft</p>
        <p class="note">**Complex floor plans are priced individually regardless of sqft.</p>
      </div>
    </section>

    <footer class="contact">
      For more information or to book a shoot please visit our website:<br>
      www.OpenGatePhotography.com or call Dana at 555-014-2277
    </footer>
    <div class="footer-band"></div>
  </main>
</body>
</html>
```